Caltrisa Website Design

Caltrisa Solutions. http://caltrisasolutions-example.com is looking to redesign our current website with a modern feel and added functionality.

The winning design will be coded in HTML 5 and be responsive built for mobile. You can use bootstrap, jquery.

Wordpress or wix will not be accepted.

Page 1
http://caltrisasolutions-example.com/

Page 2
http://caltrisasolutions-example.com/who_we_are.php

Page 3
http://caltrisasolutions-example.com/solutions_offered.php

Page 4
http://caltrisasolutions-example.com/faq.php

Here are some pages from our competitors. Please see notes of our likes and dislikes of each page.

https://www.pellorcare-example.com/

Likes: Ability to explore opportunities / “Neighbour Threads” Highlighting involvement in the community.

Dislike: Layout not very interactive. Feels clunky

https://www.vantrelmed-example.com/

Likes: Visually appealing. Using nice images.

Dislike: Not very intuitive. You need to read a bit to figure out what they do and what they’re about.. Not overly interactive either.

https://kribowork-example.com/

Likes: Clean, Using a puppy as part of marketing, highlights Stability and Quality

Dislikes: All services offered are further down and requires you click and drill down to get info

https://www.sundrilex-example.com/

Likes: Has video about Improving Coding Accuracy which is important to clients. Their “Our Solutions” Section is clear and not too wordy. Once you click on Learn More it provides good info.

Dislikes: Not as visually appealing. No wow factor. Seems a bit basic.

https://fenmorpa-example.com/

Likes: Section that allows clients to request facility analysis. Has easy to find menu dropdowns at the top of page.

Dislikes: Boring site. Nothing special at all.

https://quillbrook-example.com/

Likes: I actually like this site overall

Dislikes: It is a little busy, but other than that it’s pretty nice.

https://tazurn-example.com

Likes: although their choice of doodle graphics is overly busy, I like that it’s different from every other vendor. To me, it stands out. I also like how when you scroll, it pops up a new highlight and keeps the watermark in the background.

Dislikes: Choice of font is a lil hard to read and not easy on the eyes. I believe the bold and color of the font make it appear too busy.

https://wexlingford-example.com/

Likes: Probably my favorite. Very professional and interactive. I like how it scrolls through images at the top with links to allow you to dive in further. I also like the interactive photo blocks towards the bottom and how they use photos from past speaking events that give them credibility and highlight Dr Wexlingford speaking.

Dislikes: Nothing specific

Do to the ongoing Corona Virus here in Florida we have been dealing with that. Most will be working from home this week and plan to focus on finalizing this project. Thanks

Please extend this. With the current COVID19 stuff this is kind of been put on the back burner.

```html
<!DOCTYPE html>
<html lang="en">
<head>
<meta charset="utf-8">
<title>Caltrisa Solutions – FAQ</title>
<link href="https://fonts.googleapis.com/css2?family=Poppins:wght@400;500;600;700&display=swap" rel="stylesheet">
<style>
:root{
  --green:#8fdc8f;
  --green-dark:#6cc36c;
  --navy:#3d4aa0;
  --navy-dark:#34408f;
  --text:#222;
  --muted:#666;
  --border:#d9d9d9;
  --white:#fff;
}
*{box-sizing:border-box;margin:0;padding:0}
html,body{width:1200px;height:2254px;overflow:hidden}
body{font-family:'Poppins',sans-serif;color:var(--text);background:var(--white);position:relative}
.abs{position:absolute}

/* header */
.site-header{position:absolute;left:0;top:0;width:1200px;height:110px;background:var(--white)}
.brand{left:87px;top:24px;display:flex;align-items:center;gap:10px}
.brand-mark{width:18px;height:18px;border-radius:50%;background:var(--green-dark)}
.brand-name{font-size:30px;font-weight:600;color:var(--green-dark);letter-spacing:1px}
.topbar{left:596px;top:11px;width:416px;height:28px;border-bottom:1px solid #e2e2e2;font-size:13px;color:#555}
.topbar .dot{position:absolute;top:3px;width:9px;height:9px;border-radius:50%;background:#777}
.topbar .phone{position:absolute;right:10px;top:1px}
.topbar .phone b{font-weight:500;color:#444}
.main-nav{left:429px;top:64px;display:flex;gap:30px;font-size:13px;font-weight:500;color:#222}
.header-cta{left:1016px;top:0;width:184px;height:110px;background:var(--green)}
.header-cta span{position:absolute;left:28px;top:34px;width:129px;height:42px;border:2px solid var(--white);color:var(--white);font-size:14px;font-weight:600;display:flex;align-items:center;justify-content:center}

/* hero */
.hero{left:0;top:110px;width:1200px;height:368px;background:linear-gradient(100deg,#6e7276 0%,#9a9da2 35%,#b9bcc0 60%,#8d8a86 80%,#5c5650 100%)}
.hero h1{position:absolute;left:93px;top:130px;font-size:58px;font-weight:700;color:var(--white);letter-spacing:1px}
.crumbs{position:absolute;left:93px;top:204px;font-size:15px;color:var(--white);display:flex;gap:18px;align-items:center}
.crumbs .current{color:var(--green)}

/* headings */
.section-title{position:absolute;left:0;width:1200px;text-align:center;font-weight:700;color:var(--navy)}
.underline{position:absolute;left:580px;width:40px;height:3px;background:var(--green)}

/* faq */
.faq-item{position:absolute;left:304px;width:590px;height:46px;border:2px solid #e5e5e5;border-radius:3px;font-size:14.5px;font-weight:500;padding:12px 0 0 25px}
.toggle{position:absolute;right:16px;top:12px;width:19px;height:19px;border-radius:50%;background:#ddd;font-size:13px;line-height:19px;text-align:center;color:#333}
.faq-open{position:absolute;left:304px;top:839px;width:590px;height:253px;background:var(--green);border-radius:3px;color:var(--white);padding:18px 37px 0 26px}
.faq-open h3{font-size:14.5px;font-weight:500}
.faq-open p{font-size:13px;line-height:17.8px;margin-top:12px;text-align:justify}
.faq-open .toggle{background:var(--white);color:var(--green-dark);top:20px}

.cta-sub{position:absolute;left:0;top:1392px;width:1200px;text-align:center;font-size:15px;font-weight:500;letter-spacing:.5px}
.btn-apply{position:absolute;left:537px;top:1429px;width:131px;height:43px;background:var(--green);color:var(--white);font-size:14px;font-weight:600;display:flex;align-items:center;justify-content:center}
.people{left:0;top:1470px;width:1200px;height:366px;background:linear-gradient(180deg,#fff 0%,#e9e3df 30%,#b9a69b 60%,#4d5876 100%)}

/* footer */
.footer{left:0;top:1836px;width:1200px;height:365px;background:var(--navy);color:var(--white)}
.footer .brand-name{color:var(--white);font-size:32px}
.footer h4{position:absolute;font-size:14px;font-weight:600;top:84px;letter-spacing:.3px}
.links{position:absolute;left:373px;top:120px;font-size:13.5px;line-height:31px;list-style:none}
.contact{position:absolute;left:579px;top:120px;font-size:13.5px;line-height:22px}
.contact .row{position:relative;padding-left:23px;margin-bottom:14px}
.contact svg{position:absolute;left:0;top:4px}
.news{position:absolute;left:852px;top:120px;font-size:13.5px;line-height:18px;width:230px}
.subscribe{position:absolute;left:852px;top:171px;width:257px;height:44px;background:var(--white);display:flex;align-items:center;padding-left:36px;font-size:13px;color:#555}
.subscribe .send{position:absolute;right:0;top:0;width:40px;height:44px;background:var(--green);display:flex;align-items:center;justify-content:center}
.social{position:absolute;top:235px;width:36px;height:36px;border-radius:50%;background:rgba(255,255,255,.12)}
.social i{position:absolute;left:14px;top:14px;width:8px;height:8px;border-radius:50%;background:var(--white)}
.copyright{left:0;top:2201px;width:1200px;height:53px;background:var(--navy-dark);color:var(--white);font-size:13.5px;display:flex;align-items:center;justify-content:center}
.to-top{left:1137px;top:2183px;width:36px;height:36px;border-radius:50%;background:var(--white);display:flex;align-items:center;justify-content:center}
</style>
</head>
<body>

<header class="site-header">
  <div class="abs brand"><span class="brand-mark"></span><span class="brand-name">CALTRISA</span></div>
  <div class="abs topbar">
    <span class="dot" style="left:6px"></span>
    <span class="dot" style="left:50px"></span>
    <span class="phone">CONTACT US: <b>(555) 014-2730</b></span>
  </div>
  <nav class="abs main-nav">
    <span>HOME</span><span>JOB SEARCH</span><span>APPLY NOW</span><span>ABOUT CALTRISA</span><span>SOLUTIONS</span><span>LOGIN</span>
  </nav>
  <div class="abs header-cta"><span>CONTACT US</span></div>
</header>

<section class="abs hero" role="img" aria-label="Photo of an older doctor with glasses holding a pen, talking with a young patient">
  <h1>CALTRISA FAQ’S</h1>
  <div class="crumbs">
    <span style="display:flex;align-items:center;gap:8px">
      <svg width="17" height="15" viewBox="0 0 17 15"><path d="M8.5 0 0 7.5h2.5V15h4.5v-5h3v5h4.5V7.5H17z" fill="#fff"/></svg>HOME</span>
    <span>|</span><span class="current">FAQ’S</span>
  </div>
</section>

<h2 class="section-title" style="top:568px;font-size:31px">FREQUENTLY ASKED QUESTION’S</h2>
<div class="underline" style="top:611px"></div>

<div class="faq-item" style="top:646px">How do I start the conversation with Caltrisa Solutions?<span class="toggle">–</span></div>
<div class="faq-item" style="top:710px">What are the requirements to become a Caltrisa Solutions Consultant?<span class="toggle">–</span></div>
<div class="faq-item" style="top:774px">What are the benefits of becoming a Caltrisa Solutions consultants?<span class="toggle">–</span></div>
<div class="faq-open">
  <h3>Is there any application fees or commitment to a long term contract?</h3>
  <span class="toggle">+</span>
  <p>No. Applying is free and confidential. The terms of contracts are limited to the length of the assignment that you agree to accept. Generally speaking, contracts last 13 weeks. Many times, contracts will be renewed as long as you are still interested in working at the facility. It’s all up to you!</p>
  <p>Caltrisa Solutions biggest differentiator is our recruiting team. With more than 30 years of healthcare focused recruitment and retention this enables us to ensure that we are finding the best consultants the best projects. Caltrisa Solutions recruiting team prepares our consultants for their next project down to the smallest detail and continues to be a trusted resource through the duration of the assignment.</p>
</div>
<div class="faq-item" style="top:1107px">How do I know which assignment is right for me?<span class="toggle">–</span></div>
<div class="faq-item" style="top:1171px">If I take a travel assignment, how often am I able to come home?<span class="toggle">–</span></div>

<div class="abs people" role="img" aria-label="Photo of six smiling young people sitting together with tablets and folders, looking upward"></div>

<h2 class="section-title" style="top:1318px;font-size:38px">OPPORTUNITIES AVAILABLE IN MIAMI, FL</h2>
<div class="underline" style="top:1372px"></div>
<p class="cta-sub">CLICK BELOW TO APPLY.</p>
<div class="btn-apply">APPLY NOW</div>

<footer class="abs footer">
  <div class="abs brand" style="left:87px;top:166px"><span class="brand-mark" style="background:#fff"></span><span class="brand-name">CALTRISA</span></div>
  <h4 style="left:373px">QUICK LINKS</h4>
  <ul class="links">
    <li>Home</li><li>Job Search</li><li>Apply Now</li><li>About Caltrisa Solutions</li><li>Login</li><li>Join Commission</li>
  </ul>
  <h4 style="left:579px">CONTACT US</h4>
  <div class="contact">
    <div class="row"><svg width="14" height="11" viewBox="0 0 14 11"><rect width="14" height="11" rx="1" fill="#8fdc8f"/><path d="M0 1l7 5 7-5" stroke="#3d4aa0" fill="none"/></svg>Email:<br>jobs@caltrisasolutions-example.com</div>
    <div class="row"><svg width="14" height="14" viewBox="0 0 14 14"><path d="M3 0l2.5 3.5L4 5.5c1 2 2.5 3.5 4.5 4.5l2-1.5L14 11l-1.5 3C6 14 0 8 0 1.5z" fill="#8fdc8f"/></svg>Telephone:<br>(555) 014-2730</div>
    <div class="row"><svg width="11" height="15" viewBox="0 0 11 15"><path d="M5.5 0A5.5 5.5 0 0 0 0 5.5C0 10 5.5 15 5.5 15S11 10 11 5.5A5.5 5.5 0 0 0 5.5 0z" fill="#8fdc8f"/><circle cx="5.5" cy="5.5" r="2" fill="#3d4aa0"/></svg>Location:<br>4420 Harbor Crest Rd Suite 118<br>Lake Verona, FL 33901</div>
  </div>
  <h4 style="left:852px;top:86px">NEWSLETTER</h4>
  <p class="news">Subscribe to our email address to get the latest news.</p>
  <div class="subscribe">
    <svg class="abs" style="left:14px;top:17px" width="13" height="10" viewBox="0 0 13 10"><rect width="13" height="10" fill="#ccc"/><path d="M0 0l6.5 5L13 0" stroke="#fff" fill="none"/></svg>
    Enter Your Email...
    <span class="send"><svg width="18" height="16" viewBox="0 0 18 16"><path d="M0 7l18-7-4 16-5-5-3 4V10z" fill="#fff"/></svg></span>
  </div>
  <span class="social" style="left:853px"><i></i></span>
  <span class="social" style="left:894px"><i></i></span>
</footer>
<div class="abs copyright">2020 © Caltrisa Solutions, Inc</div>
<div class="abs to-top"><svg width="10" height="13" viewBox="0 0 10 13"><path d="M5 1v12M1 5l4-4 4 4" stroke="#333" fill="none" stroke-width="1.3"/></svg></div>

</body>
</html>
```